Lydia Vandermere personal business/name cards and stationery brief

I am looking for a simple design on my personal business cards, that I may use for all my stationery. All my stationery would be cream or ivory textured card, or cream/ivory quality paper. I am director of my family company and also property developer. But am wishing to have basic business cards that I can use across both businesses. I do not wish to have a title, just my initials as a focal point.
Target Market(s)
These are my personal business cards and stationery. I am looking for an elegant, relatively understated design that exudes wealth. There is no target audience, other than clients or people I already do business with. However design must be stylish and timeless.
If I am handing out my business card to anyone I do not do business with, or they are not contracting to me or my company currently, then i would like the target audience to wish they were.
I am 54 yeas of age, and my business cards must denote respect and class.
Industry/Entity Type
Business
Contact Information for Business Card
LV
Lydia Vandermere
Justice of the Peace
Possible rear of card
Mobile number
Email
Font styles to use
Requirements
Must have
- LV to be somehow entwined as a logo on the front of the card above my name
- These cards must state that I am a Justice of the Peace
- Colours only ivory or cream card with texture, and gold elegant font.
- Must be able to be used on all my stationery products
- Must be elegant, timeless and not cluttered
- Below are just some design I like. There is something in each design I like.
Nice to have
- I would like my initials to be the centre piece of the card. Somehow entwined together elegantly in a logo of sorts that I can use across all my stationery. But if not my initials, then something that is different and stands out from the rest.
Should not have
- Not gawdy or young. No colour. Nothing outlandish.

```html
<!DOCTYPE html>
<html lang="en">
<head>
<meta charset="utf-8">
<title>Lydia Vandermere — Business Card</title>
<link href="https://fonts.googleapis.com/css2?family=Cookie&family=Cormorant+Garamond:wght@400;500&family=Cinzel:wght@500&family=Playfair+Display:wght@500&display=swap" rel="stylesheet">
<style>
  :root {
    --backdrop: #1b1b1b;
    --ivory-light: #fffffa;
    --ivory-warm: #fbf6dc;
    --gold-light: #fdf6d2;
    --gold-mid: #f8e8a6;
    --gold-deep: #f1dc89;
    --ink: #1e1c19;
    --ink-soft: #3a3630;
    --watermark: rgba(236, 214, 140, 0.28);
  }
  * { margin: 0; padding: 0; box-sizing: border-box; }
  html, body { width: 1200px; height: 1200px; overflow: hidden; background: var(--backdrop); }
  .canvas { position: relative; width: 1200px; height: 1200px; }

  .card {
    position: absolute;
    left: 250px;
    width: 700px;
    height: 400px;
    border-radius: 44px;
    overflow: hidden;
  }

  /* Front: details side */
  .card--details {
    top: 150px;
    background: linear-gradient(135deg, var(--ivory-warm) 0%, var(--ivory-light) 45%, var(--ivory-warm) 100%);
  }
  .card--details .rules { position: absolute; inset: 0; }
  .dove-watermark {
    position: absolute;
    right: 60px; top: 40px;
    width: 230px; height: 220px;
    border-radius: 50%;
    background: radial-gradient(ellipse at center, var(--watermark) 0%, rgba(255,255,255,0) 70%);
  }
  .scales-emblem {
    position: absolute;
    left: 45px; top: 70px;
    width: 90px; height: 58px;
    background: linear-gradient(180deg, #4a453d, var(--ink));
    border-radius: 6px;
    opacity: 0.85;
  }
  .holder-name {
    position: absolute;
    left: 190px; right: 40px; top: 62px;
    text-align: center;
    font-family: "Cookie", cursive;
    font-size: 58px;
    color: var(--ink);
    letter-spacing: 1px;
  }
  .holder-role {
    position: absolute;
    left: 190px; right: 40px; top: 150px;
    text-align: center;
    font-family: "Cormorant Garamond", serif;
    font-size: 22px;
    color: var(--ink-soft);
  }
  .contact-list {
    position: absolute;
    left: 200px; top: 270px;
    list-style: none;
    font-family: "Cormorant Garamond", serif;
    font-size: 19px;
    color: var(--ink);
  }
  .contact-list li { display: flex; align-items: center; gap: 10px; height: 28px; }
  .contact-list svg { width: 15px; height: 15px; fill: var(--ink); flex: none; }

  /* Back: monogram side */
  .card--monogram {
    top: 650px;
    background: linear-gradient(100deg, var(--gold-mid) 0%, var(--gold-light) 50%, var(--gold-deep) 100%);
  }
  .dove-emblem {
    position: absolute;
    left: 220px; top: 30px;
    width: 300px; height: 230px;
    border-radius: 50%;
    background: radial-gradient(ellipse at center, rgba(255, 250, 220, 0.7) 0%, rgba(255,250,220,0) 70%);
  }
  .monogram {
    position: absolute;
    left: 0; right: 0; top: 70px;
    text-align: center;
    font-family: "Playfair Display", serif;
    font-weight: 500;
    font-size: 150px;
    line-height: 1;
    color: var(--ink);
  }
  .monogram-name {
    position: absolute;
    left: 0; right: 0; top: 285px;
    text-align: center;
    font-family: "Cinzel", serif;
    font-weight: 500;
    font-size: 36px;
    letter-spacing: 3px;
    color: var(--ink);
  }
</style>
</head>
<body>
<main class="canvas">

  <section class="card card--details">
    <div class="dove-watermark" role="img" aria-label="Faint dove with olive branch watermark"></div>
    <svg class="rules" viewBox="0 0 700 400" aria-hidden="true">
      <line x1="150" y1="45" x2="170" y2="380" stroke="#1e1c19" stroke-width="4" stroke-linecap="round"/>
      <line x1="40" y1="140" x2="650" y2="140" stroke="#1e1c19" stroke-width="4" stroke-linecap="round"/>
    </svg>
    <div class="scales-emblem" role="img" aria-label="Scales of justice emblem"></div>
    <h1 class="holder-name">Lydia Vandermere</h1>
    <p class="holder-role">Justice of the Peace</p>
    <ul class="contact-list">
      <li><svg viewBox="0 0 16 16"><rect x="4" y="1" width="8" height="14" rx="1.5"/></svg>1-555-204817</li>
      <li><svg viewBox="0 0 16 16"><circle cx="8" cy="8" r="7"/></svg>hello@vandermerehouse.com</li>
      <li><svg viewBox="0 0 16 16"><path d="M8 1a5 5 0 0 0-5 5c0 4 5 9 5 9s5-5 5-9a5 5 0 0 0-5-5zm0 7a2 2 0 1 1 0-4 2 2 0 0 1 0 4z"/></svg>Harlow Bay, Westmere Land</li>
    </ul>
  </section>

  <section class="card card--monogram">
    <div class="dove-emblem" role="img" aria-label="Embossed dove with olive branch"></div>
    <div class="monogram">LV</div>
    <p class="monogram-name">LYDIA VANDERMERE</p>
  </section>

</main>
</body>
</html>
```